regPersonal Trainer Flyer Design

Reason: I have been very busy with other work and would like to extend the deadline to offer designers the chance to edit and improve designs with my help. Thank you for all the designs that have been sent so far.

```html
<!DOCTYPE html>
<html lang="en">
<head>
<meta charset="utf-8">
<title>Personal Trainer Flyer</title>
<link rel="stylesheet" href="https://fonts.googleapis.com/css2?family=Barlow:wght@400;600;700&family=Comic+Neue:wght@700&display=swap">
<style>
  :root {
    --brand-blue: #1670b8;
    --paper: #f3f3f3;
    --ink-black: #111111;
    --white: #ffffff;
    --stage: #e6e6e6;
    --photo-tone-a: #8a8f96;
    --photo-tone-b: #c9c2bd;
  }
  * { margin: 0; padding: 0; box-sizing: border-box; }
  html, body { width: 1200px; height: 1000px; overflow: hidden; }
  body { background: var(--stage); font-family: "Barlow", Arial, sans-serif; position: relative; }

  .flyer {
    position: absolute; left: 40px; top: 104px;
    width: 1120px; height: 792px;
    background: var(--paper); overflow: hidden;
  }
  .flyer > * { position: absolute; }

  .portrait-blob { left: 0; top: 40px; width: 190px; height: 100px; }
  .portrait {
    left: 61px; top: 13px; width: 186px; height: 186px; border-radius: 50%;
    border: 5px solid var(--brand-blue);
    background: radial-gradient(circle at 50% 40%, var(--photo-tone-b), var(--photo-tone-a) 70%);
  }

  .trainer-name { left: 273px; top: 52px; font-size: 45px; font-weight: 400; color: var(--brand-blue); line-height: 1; }
  .phone-head { left: 743px; top: 52px; display: flex; align-items: center; gap: 22px; }
  .phone-head .icon { width: 40px; height: 40px; }
  .phone-head .number { font-size: 42px; font-weight: 700; color: var(--brand-blue); line-height: 1; letter-spacing: 1px; }
  .headline { left: 271px; top: 100px; font-size: 78px; font-weight: 700; color: var(--brand-blue); line-height: 1; white-space: nowrap; }

  .question-band { left: 0; top: 226px; width: 1120px; height: 202px; }
  .question {
    font-family: "Comic Neue", "Comic Sans MS", cursive;
    font-weight: 700; font-size: 45px; color: var(--white);
    transform: rotate(-3.5deg); transform-origin: left center; white-space: nowrap; line-height: 1;
  }
  .q1 { left: 20px; top: 262px; }
  .q2 { left: 312px; top: 300px; }
  .q3 { left: 685px; top: 338px; }

  .need-help {
    left: 19px; top: 440px; font-family: "Comic Neue", "Comic Sans MS", cursive;
    font-weight: 700; font-size: 70px; color: var(--brand-blue); line-height: 1;
  }

  .benefits-panel {
    left: 0; top: 544px; width: 814px; height: 248px;
    background: var(--brand-blue); border-top-right-radius: 14px;
  }
  .benefits { list-style: none; left: 24px; top: 590px; }
  .benefits li {
    display: flex; align-items: center; gap: 12px; color: var(--white);
    font-size: 34px; font-weight: 400; height: 34px; white-space: nowrap;
  }
  .benefits li + li { margin-top: 30px; }
  .benefits li:last-child { margin-top: 37px; }
  .benefits .tick { width: 30px; height: 30px; flex: none; }

  .session-photo {
    left: 500px; top: 450px; width: 282px; height: 187px; border-radius: 10px;
    border: 3px solid var(--white);
    background: linear-gradient(135deg, var(--photo-tone-b), var(--photo-tone-a));
  }

  .figure-art { left: 904px; top: 500px; width: 90px; height: 123px; border-radius: 8px; background: var(--brand-blue); opacity: 0.85; }

  .contact-card { left: 837px; top: 636px; color: var(--brand-blue); }
  .contact-card .role { font-size: 25px; font-weight: 400; line-height: 1.2; }
  .contact-card .name { font-size: 26px; font-weight: 700; line-height: 1.2; }
  .contact-card .line { display: flex; align-items: center; gap: 6px; font-size: 19px; line-height: 1.35; }
  .contact-card .line:first-of-type { margin-top: 22px; }
  .contact-card .line svg { width: 16px; height: 16px; flex: none; }
</style>
</head>
<body>
<main class="flyer">
  <svg class="portrait-blob" viewBox="0 0 190 100" aria-hidden="true">
    <path d="M0 10 C40 -6 110 0 150 20 L190 60 C170 95 100 104 40 96 C10 92 0 80 0 70 Z" fill="var(--brand-blue)"/>
  </svg>
  <div class="portrait" role="img" aria-label="Round portrait photo of the trainer in the gym"></div>

  <p class="trainer-name">Sam Holloway</p>
  <div class="phone-head">
    <svg class="icon" viewBox="0 0 40 40" aria-hidden="true">
      <rect width="40" height="40" rx="6" fill="var(--brand-blue)"/>
      <path d="M13 9 l5 0 2 7 -3 3 c2 4 4 6 8 8 l3 -3 7 2 0 5 c0 2 -2 3 -4 3 C18 34 6 22 6 13 c0 -2 2 -4 4 -4 Z" fill="var(--white)" transform="translate(0 -1) scale(0.95)"/>
    </svg>
    <span class="number">07700900418</span>
  </div>
  <h1 class="headline">Your Personal Trainer</h1>

  <svg class="question-band" viewBox="0 0 1120 202" preserveAspectRatio="none" aria-hidden="true">
    <path fill="var(--ink-black)" d="M0 30 L20 18 L60 24 L80 12 L140 20 L220 8 L300 16 L420 4 L600 10 L800 4 L960 8 L1080 6 L1120 4 L1120 150 L1104 160 L1112 174 L1090 178 L1060 184 L900 180 L780 186 L740 174 L560 178 L380 172 L250 178 L140 170 L100 190 L70 176 L30 186 L0 180 Z"/>
  </svg>
  <p class="question q1">Lacking motivation?</p>
  <p class="question q2">Not achieving your goals?</p>
  <p class="question q3">Bored of the gym?</p>

  <p class="need-help">Need help???</p>

  <div class="benefits-panel"></div>
  <div class="session-photo" role="img" aria-label="Photo of the trainer coaching a client through a barbell squat"></div>
  <ul class="benefits">
    <li><svg class="tick" viewBox="0 0 30 30" aria-hidden="true"><circle cx="15" cy="15" r="14" fill="var(--white)"/><path d="M8 15 l5 5 9 -10" stroke="var(--brand-blue)" stroke-width="3.5" fill="none" stroke-linecap="round" stroke-linejoin="round"/></svg>You’re never too old</li>
    <li><svg class="tick" viewBox="0 0 30 30" aria-hidden="true"><circle cx="15" cy="15" r="14" fill="var(--white)"/><path d="M8 15 l5 5 9 -10" stroke="var(--brand-blue)" stroke-width="3.5" fill="none" stroke-linecap="round" stroke-linejoin="round"/></svg>I can help improve your health and well-being</li>
    <li><svg class="tick" viewBox="0 0 30 30" aria-hidden="true"><circle cx="15" cy="15" r="14" fill="var(--white)"/><path d="M8 15 l5 5 9 -10" stroke="var(--brand-blue)" stroke-width="3.5" fill="none" stroke-linecap="round" stroke-linejoin="round"/></svg>Training can be at your home</li>
  </ul>

  <div class="figure-art" role="img" aria-label="Blue silhouette of an athlete doing a handstand"></div>

  <div class="contact-card">
    <p class="role">Personal Trainer</p>
    <p class="name">Sam Holloway</p>
    <p class="line"><svg viewBox="0 0 16 16" aria-hidden="true"><rect width="16" height="16" rx="3" fill="var(--brand-blue)"/><path d="M5 3 h2 l1 3 -1.3 1.2 c.8 1.6 1.6 2.4 3.2 3.2 L11 9 l3 1 v2 c0 1-1 1.5-2 1.5 C7 13.5 2.5 9 2.5 5 c0-1 .5-2 1.5-2 Z" fill="var(--white)"/></svg>07700900418</p>
    <p class="line"><svg viewBox="0 0 16 16" aria-hidden="true"><rect y="2" width="16" height="12" rx="1.5" fill="var(--brand-blue)"/><path d="M1 4 l7 5 7 -5" stroke="var(--white)" stroke-width="1.5" fill="none"/></svg>samholloway@mailbox.co.uk</p>
  </div>
</main>
</body>
</html>
```